Antibacterial Hand Wash Squeeze Tube Label

We're looking for a contemporary label design for a new Antibacterial Hand Wash for an 8oz squeeze tube. The new consumer brand will be sold to consumers in major US retail stores & online. The moisturizing hand wash contains Aloe Vera, vitamin E, and other natural ingredients so the design should include the color green. Real photos are very effective on packaging, so a picture of Aloe Vera or possibly two hands washing would help draw consumers' attention to the tube on the retail shelf. The front label may wrap around the sides. Rear must be left mostly blank
US Consumers - retail stores & online
Consumer

```html
<!DOCTYPE html>
<html lang="en">
<head>
<meta charset="utf-8">
<title>Verdane Natural Handwash – Tube Label</title>
<link href="https://fonts.googleapis.com/css2?family=Cinzel:wght@600&family=Cormorant+Garamond:ital,wght@1,600&family=Roboto+Condensed:wght@400&display=swap" rel="stylesheet">
<style>
  :root {
    --bg: #ffffff;
    --label: #f7f7f7;
    --label-edge: #e6e6e6;
    --green: #7aa32c;
    --green-deep: #3f8f1f;
    --grey-text: #6b6b6b;
    --dark-text: #333333;
    --rule: #9a9a9a;
    --white: #ffffff;
  }
  * { margin: 0; padding: 0; box-sizing: border-box; }
  html, body { width: 1200px; height: 849px; overflow: hidden; background: var(--bg); }
  .canvas { position: relative; width: 1200px; height: 849px; }

  .label {
    position: absolute;
    top: 104px;
    width: 254px;
    height: 536px;
    background: var(--label);
    border: 1px solid var(--label-edge);
  }
  .label--front { left: 262px; }
  .label--back { left: 636px; }

  /* Front panel */
  .brand-front {
    position: absolute;
    top: 96px; left: 0; width: 100%;
    text-align: center;
    font-family: "Cinzel", serif;
    font-weight: 600;
    font-size: 36px;
    letter-spacing: 1px;
    color: var(--green-deep);
  }
  .tagline-front {
    position: absolute;
    top: 137px; left: 48px;
    font-family: "Cormorant Garamond", serif;
    font-style: italic;
    font-weight: 600;
    font-size: 12px;
    color: var(--grey-text);
  }
  .hero-visual {
    position: absolute;
    top: 158px; left: 78px;
    width: 100px; height: 282px;
    border-radius: 40px 40px 30px 30px;
    background: linear-gradient(180deg, #d8efb8 0%, #6cb83a 25%, #3d8f22 38%, #a9d77a 60%, #e9c9ae 82%, #f2f2f2 100%);
  }
  .claims {
    position: absolute;
    top: 446px; left: 0; width: 100%;
    text-align: center;
    font-family: "Roboto Condensed", sans-serif;
  }
  .claims__rule { width: 36px; height: 1px; background: var(--rule); margin: 0 auto 4px; }
  .claims__rule--wide { width: 72px; margin: 3px auto 0; }
  .claims__main { font-size: 11px; color: var(--grey-text); letter-spacing: .3px; }
  .claims__accent { font-size: 11px; color: var(--green); letter-spacing: .3px; }
  .net-weight { margin-top: 15px; font-size: 9px; color: var(--dark-text); }

  /* Back panel */
  .brand-band {
    position: absolute;
    top: 0; left: 70px;
    width: 90px; height: 100%;
    background: var(--green);
  }
  .brand-vertical {
    position: absolute;
    left: 115px; top: 300px;
    transform: translate(-50%, -50%) rotate(-90deg);
    font-family: "Cinzel", serif;
    font-weight: 600;
    font-size: 66px;
    color: var(--white);
    white-space: nowrap;
  }
  .tagline-vertical {
    position: absolute;
    left: 183px; top: 392px;
    transform: translate(-50%, -50%) rotate(-90deg);
    font-family: "Cormorant Garamond", serif;
    font-style: italic;
    font-weight: 600;
    font-size: 24px;
    color: var(--grey-text);
    white-space: nowrap;
  }
  .side-visual {
    position: absolute;
    top: 118px; left: 168px;
    width: 66px; height: 150px;
    border-radius: 24px 24px 16px 16px;
    background: linear-gradient(180deg, #d8efb8 0%, #5cae30 35%, #a9d7e6 60%, #e9c9ae 80%, #f2f2f2 100%);
  }
</style>
</head>
<body>
<main class="canvas">
  <section class="label label--front">
    <div class="brand-front">VERDANE</div>
    <div class="tagline-front">Natural Handwash</div>
    <div class="hero-visual" role="img" aria-label="Photo of a fresh aloe vera plant with green swirls above cupped hands under running water"></div>
    <div class="claims">
      <div class="claims__rule"></div>
      <p class="claims__main">99% ALOEBERA GEL</p>
      <p class="claims__accent">PARABEN FREE</p>
      <div class="claims__rule claims__rule--wide"></div>
      <p class="net-weight">NET WT 2.OZ (50g)</p>
    </div>
  </section>

  <section class="label label--back">
    <div class="brand-band"></div>
    <div class="brand-vertical">VERDANE</div>
    <div class="tagline-vertical">Natural Handwash</div>
    <div class="side-visual" role="img" aria-label="Small photo of an aloe vera plant above cupped hands with water"></div>
  </section>
</main>
</body>
</html>
```